Willow Creek Haven website design

To create 2 pages (a front page and sub page) for a health/spiritual website. I have a logo, and was thinking of incorporating Greek temple columns in the design or something similar, but open to other ideas.

The design should suit mobile devices with limited screen space also.

Industry/Entity Type

Health

Number of Pages Required

1 page

```html
<!DOCTYPE html>
<html lang="en">
<head>
<meta charset="utf-8">
<title>Willow Creek Haven</title>
<link rel="stylesheet" href="https://fonts.googleapis.com/css2?family=Montserrat:wght@400;600&family=Cardo:wght@400&family=Cabin:wght@400;500&display=swap">
<style>
:root{
  --sky:#9dd6e4;
  --header:#a3d9e5;
  --teal:#22a3bf;
  --teal-dark:#1a8ba5;
  --ink:#2f3a40;
  --text:#3b4449;
  --white:#ffffff;
  --footer-top:#56687a;
  --footer-bottom:#3c4e5c;
}
*{margin:0;padding:0;box-sizing:border-box}
html,body{width:1200px;height:2647px;overflow:hidden}
body{position:relative;background:var(--sky);font-family:"Cabin",sans-serif;color:var(--text)}
.abs{position:absolute}

.site-header{left:0;top:0;width:1200px;height:110px;background:var(--header)}
.brand-mark{left:74px;top:21px;width:56px;height:56px;background:#1f2326}
.brand-name{left:145px;top:34px;font-family:"Montserrat",sans-serif;font-weight:600;font-size:24px;color:#2c3538}
.social{top:30px;width:32px;height:32px;border-radius:50%;background:#2479b5}

.hero{left:0;top:110px;width:1200px;height:638px;
  background:radial-gradient(ellipse 260px 380px at 620px 170px,#ffffff 0%,#d9f1f5 25%,#7fc4cf 55%,#2b8b99 80%,#0f5463 100%)}
.main-nav{left:109px;top:141px;width:971px;height:67px;background:rgba(235,245,248,.85);
  box-shadow:0 6px 10px rgba(0,0,0,.35);display:flex;align-items:center}
.main-nav a{position:absolute;font-family:"Montserrat",sans-serif;font-size:22px;color:#2f3a40;text-decoration:none}

.feature{border:3px solid var(--white)}
.feature-img{background:#333}
h2.feature-title{font-family:"Cardo",serif;font-weight:400;font-size:27px;color:var(--ink)}
.feature-text{font-size:14px;line-height:19.5px;color:var(--text)}
.btn{background:var(--teal);color:var(--white);font-size:12px;font-weight:500;display:flex;align-items:center;justify-content:center;box-shadow:0 2px 3px rgba(0,0,0,.25);border-radius:2px}

.section-title{left:168px;top:1447px;font-family:"Cardo",serif;font-size:20px;color:var(--ink)}
.card-img{width:132px;height:88px}
.card-text{width:212px;font-size:14px;line-height:19.5px}

.join-bar{left:168px;top:1915px;width:850px;height:79px;background:var(--teal);border-radius:14px}
.join-text{left:194px;top:1942px;font-family:"Montserrat",sans-serif;font-size:19px;color:var(--white)}
.join-btn{left:861px;top:1931px;width:133px;height:48px;border:3px solid var(--white);color:var(--white);
  font-family:"Montserrat",sans-serif;font-weight:600;font-size:21px;display:flex;align-items:center;justify-content:center}

.site-footer{left:0;top:2062px;width:1200px;height:585px;
  background:linear-gradient(180deg,var(--footer-top) 0%,#6b7a84 45%,var(--footer-bottom) 100%)}
.footer-head{top:2226px;font-family:"Cabin",sans-serif;font-size:18px;color:var(--white)}
.footer-text{top:2265px;width:180px;font-size:14px;line-height:19.5px;color:var(--white)}
.footer-text p+p{margin-top:9px}
.field{left:861px;width:157px;height:28px;border:2px solid var(--white);color:var(--white);font-size:11px;padding:5px 6px}
.submit{left:861px;top:2361px;width:67px;height:22px;border:1px solid var(--white);color:var(--white);font-size:11px;padding:3px 5px}
.footer-rule{left:168px;top:2593px;width:850px;height:1px;background:rgba(255,255,255,.55)}
.copyright{left:0;top:2613px;width:1200px;text-align:center;font-size:14px;color:var(--white)}
</style>
</head>
<body>

<header>
  <div class="abs site-header"></div>
  <div class="abs brand-mark"></div>
  <div class="abs brand-name">Willow Creek Haven</div>
  <span class="abs social" style="left:941px"></span>
  <span class="abs social" style="left:978px;background:#2fa6dc"></span>
  <span class="abs social" style="left:1015px;background:#c9412f"></span>
</header>

<section class="abs hero" role="img" aria-label="Glowing human figure walking out of radiant light among sparkling stars"></section>
<nav class="abs main-nav">
  <a href="#" style="left:141px">Home</a>
  <a href="#" style="left:237px">About us</a>
  <a href="#" style="left:385px">Foundations Program</a>
  <a href="#" style="left:641px">Services</a>
  <a href="#" style="left:761px">Contact</a>
</nav>

<main>
  <article class="abs feature" style="left:168px;top:810px;width:852px;height:270px"></article>
  <div class="abs feature-img" role="img" aria-label="Meditating silhouette with glowing chakra points" style="left:189px;top:824px;width:328px;height:219px;background:radial-gradient(circle at 50% 45%,#6c7fb0,#2a3258 70%,#161a30)"></div>
  <h2 class="abs feature-title" style="left:565px;top:822px">Lorem Ipsum</h2>
  <p class="abs feature-text" style="left:565px;top:860px;width:415px">Lorem Ipsum is simply dummy text of the printing and typesetting industry. Lorem Ipsum has been the industry's standard dummy text ever since the 1500s, when an unknown printer took a galley of type and scrambled it to make a type specimen book. It has survived not only five centuries, but also the leap into electronic typesetting, remaining essentially unchanged.Lorem Ipsum is simply dummy text of the printing and typesetting industry. Lorem Ipsum has been the industry's standard dummy text ever since the 1500s, when an unknown printer took a galley</p>
  <a class="abs btn" style="left:881px;top:1036px;width:95px;height:34px">Read more</a>

  <article class="abs feature" style="left:168px;top:1131px;width:852px;height:272px"></article>
  <h2 class="abs feature-title" style="left:189px;top:1140px">Lorem Ipsum</h2>
  <p class="abs feature-text" style="left:189px;top:1178px;width:415px">Lorem Ipsum is simply dummy text of the printing and typesetting industry. Lorem Ipsum has been the industry's standard dummy text ever since the 1500s, when an unknown printer took a galley of type and scrambled it to make a type specimen book. It has survived not only five centuries, but also the leap into electronic typesetting, remaining essentially unchanged.Lorem Ipsum is simply dummy text of the printing and typesetting industry. Lorem Ipsum has been the industry's standard dummy text ever since the</p>
  <div class="abs feature-img" role="img" aria-label="Person meditating on a wooden deck in a green garden" style="left:641px;top:1151px;width:333px;height:222px;background:linear-gradient(160deg,#5d8f3a,#2f5e22 60%,#4a6b33)"></div>
  <a class="abs btn" style="left:189px;top:1357px;width:93px;height:34px">Read more</a>

  <h3 class="abs section-title" style="font-weight:400">Lorem Ipsum is simply dummy text of the</h3>

  <div class="abs card-img" role="img" aria-label="Hand in meditation pose by the sea" style="left:169px;top:1500px;background:linear-gradient(180deg,#b9d0d8,#8aa7b2)"></div>
  <p class="abs card-text" style="left:339px;top:1497px">Lorem Ipsum is simply dummy text of the printing and typeset-ting industry. Lorem Ipsum has been the industry's standard dummy text ever since the 1500s,</p>
  <a class="abs btn" style="left:339px;top:1627px;width:93px;height:34px">Read more</a>

  <div class="abs card-img" role="img" aria-label="Prayer beads and cross on white cloth" style="left:604px;top:1500px;background:linear-gradient(180deg,#f0ece8,#d9c9bd)"></div>
  <p class="abs card-text" style="left:773px;top:1497px">Lorem Ipsum is simply dummy text of the printing and typeset-ting industry. Lorem Ipsum has been the industry's standard dummy text ever since the 1500s,</p>
  <a class="abs btn" style="left:773px;top:1627px;width:93px;height:34px">Read more</a>

  <div class="abs card-img" role="img" aria-label="Candle lit beside an open book in the dark" style="left:169px;top:1703px;background:radial-gradient(circle at 30% 40%,#c9822f,#3a2210 50%,#120904)"></div>
  <p class="abs card-text" style="left:339px;top:1700px">Lorem Ipsum is simply dummy text of the printing and typeset-ting industry. Lorem Ipsum has been the industry's standard dummy text ever since the 1500s,</p>
  <a class="abs btn" style="left:339px;top:1829px;width:93px;height:34px">Read more</a>

  <div class="abs card-img" role="img" aria-label="Person praying in warm light" style="left:604px;top:1698px;background:linear-gradient(120deg,#3a1e10,#a8642e 60%,#e8b774)"></div>
  <p class="abs card-text" style="left:773px;top:1700px">Lorem Ipsum is simply dummy text of the printing and typeset-ting industry. Lorem Ipsum has been the industry's standard dummy text ever since the 1500s,</p>
  <a class="abs btn" style="left:773px;top:1829px;width:93px;height:34px">Read more</a>

  <div class="abs join-bar"></div>
  <p class="abs join-text">Lorem Ipsum is simply dummy text of</p>
  <a class="abs join-btn">Join us</a>
</main>

<footer>
  <div class="abs site-footer" role="img" aria-label="Ancient Greek temple columns under a grey sky"></div>

  <h4 class="abs footer-head" style="left:168px;font-weight:400">About us</h4>
  <div class="abs footer-text" style="left:168px;width:178px">
    <p>Lorem Ipsum is simply dummy text of the printing and typesetting industry. Lorem Ipsum has been the industry's standard dummy text ever since the 1500s,</p>
    <p>Lorem Ipsum is simply dummy text of the printing and typesetting industry. Lorem Ipsum has been the industry's standard dummy text ever since the 1500s,</p>
  </div>

  <h4 class="abs footer-head" style="left:443px;font-weight:400">Usefull Links</h4>
  <div class="abs footer-text" style="left:443px;width:140px">Sit avertas dero tasero yaendala mi aseay mertase deles neory kastreas verode fase laisuase avertelero ferose taserto yndolase mertaeleras neory verode fertase</div>

  <h4 class="abs footer-head" style="left:655px;font-weight:400">Services</h4>
  <div class="abs footer-text" style="left:655px;width:140px">Sit avertas dero taserto yaendala mi aseay mertase deles neory kastreas verode fase laisuase avertelero ferose taserto yndolase mertaeleras neory verode fertase</div>

  <h4 class="abs footer-head" style="left:861px;font-weight:400">News letter</h4>
  <div class="abs field" style="top:2275px">Name</div>
  <div class="abs field" style="top:2319px">E-mail</div>
  <div class="abs submit">Submit</div>

  <div class="abs footer-rule"></div>
  <p class="abs copyright">@ Privacy polecy 2016</p>
</footer>

</body>
</html>
```